Fern Ledge Maplecrest Music Festival Poster

We are a summer music festival with concerts spanning Jazz, Cabaret, Education, Broadway, Chamber and Opera. We are looking for our key art for the 2016 season. This design will serve as the basis for all promotional materials, the concert program, and our web materials. Though eventually this means we will need to adjust the design to fit many different sizes, our poster will be printed mostly on 8.5" x 11" paper, and we can adapt from there. The design will be featured online and in print. It should be vertical and not landscape.

WE ARE SEEKING SLEEK, ELEGANT DESIGNS WITH MAYBE A KEY STOCK PHOTOGRAPH AND THE RELEVANT TEXT/DETAILS.

PLEASE NOTE: The included file "avenir logo.psd" is just a suggestion for the feel we are going for. It is our "working logo" after having scraped our old logo. We are interested in seeing your own ideas on how to style the brand name, but if you have ideas working with this version of the logo, feel free to use it.

REQUIRED DETAILS:
Festival Name: Fern Ledge Maplecrest Music Festival
Dates: July 29 - August 7 2016 (the year, 2016, must be included on the poster, but it does not need to be in the same location as where the actual dates are listed)
Website: www.fernledgemaplecrestfest.example

Additional Information:
- the 7 musical styles (jazz, choral, cabaret, education, broadway, chamber, opera) are important to defining who we are. You may decide to include these on the poster.
- We are looking for a very elegant design

TARGET:
We depend highly on an older clientele. We are working to expand our brand into younger demographics, but we want to be sure that we do not alienate our current consumer base with text that may be difficult for them to read.
Updates

Project Deadline Extended Reason: I am extending the deadline because it is taking longer to get feedback from my superiors than I had expected. Extending the deadline will give me time to provide adequate feedback from the people who will ultimately be making the decision. Thank you. Added Saturday, January 30, 2016

Sorry for the delay. There were issues with the decision makers but we are selecting in the next 24 hours.

Target Market(s)

Lovers of the styles of music we feature. We have a good number of elderly consumers, but also families and school groups (discussed further in description section)

Industry/Entity Type

Entertainment

Font styles to use
Sans Serif

Requirements
Must have
• Festival Name: Fern Ledge Maplecrest Music Festival
• Dates: July 29 - August 7 2016 (the year, 2016, must be included on the poster, but it does not need to be in the same location as where the actual dates are listed)
• Website: www.fernledgemaplecrestfest.example
Nice to have
• - the 7 musical styles (jazz, choral, cabaret, education, broadway, chamber, opera) are important to defining who we are. We would love to include these styles somewhere on the image, or feature them somehow in the artwork
• - Our brand has an elegance to it due to the type of music we offer, and our location being in a very natural space. inclusion of the music/nature mixed aspect of our brand in artwork might be nice
Should not have
• Anything that may offend or alienate an older, more conservative demographic

```html
<!DOCTYPE html>
<html lang="en">
<head>
<meta charset="utf-8">
<title>Fern Ledge Maplecrest Music Festival 2016</title>
<link href="https://fonts.googleapis.com/css2?family=Oswald:wght@300;400;500&family=Cormorant+Garamond:wght@500;600&display=swap" rel="stylesheet">
<style>
  :root {
    --stage: #1a1a1a;
    --teal-top: #2f6b5c;
    --teal-mid: #234f4c;
    --navy: #0d1a2a;
    --navy-deep: #070d17;
    --gold: #d9b46a;
    --gold-dark: #8a6428;
    --silver: #c9cfc9;
    --mist: #aeb8b4;
    --sky-text: #8fb6d6;
    --year-fill: #1a2336;
    --year-edge: #e8c48a;
    --box-line: #7d8ba0;
    --genre: #e9e2d2;
  }
  * { margin: 0; padding: 0; box-sizing: border-box; }
  html, body {
    width: 992px; height: 1200px; overflow: hidden;
    background: var(--stage);
  }
  .poster {
    position: absolute; left: 125px; top: 20px;
    width: 742px; height: 1160px; overflow: hidden;
    background:
      radial-gradient(ellipse 70% 40% at 30% 12%, rgba(80,140,110,.55), transparent 70%),
      radial-gradient(ellipse 60% 35% at 85% 20%, rgba(40,90,80,.5), transparent 70%),
      linear-gradient(180deg, var(--teal-top) 0%, var(--teal-mid) 30%, #1c3a44 55%, var(--navy) 78%, var(--navy-deep) 100%);
    text-align: center;
  }
  .poster::after {
    content: ""; position: absolute; inset: 0; pointer-events: none;
    background: radial-gradient(ellipse 75% 70% at 50% 45%, transparent 55%, rgba(0,0,0,.55) 100%);
  }
  .scene-art {
    position: absolute; left: 0; top: 420px; width: 742px; height: 500px;
    background:
      radial-gradient(ellipse 40% 30% at 50% 62%, rgba(214,150,110,.55), transparent 75%),
      radial-gradient(ellipse 25% 40% at 18% 45%, rgba(20,30,40,.7), transparent 75%),
      radial-gradient(ellipse 25% 40% at 84% 45%, rgba(20,30,40,.7), transparent 75%),
      linear-gradient(180deg, rgba(60,80,90,.2), rgba(120,90,90,.35) 55%, rgba(10,20,35,.2));
  }
  .festival-name {
    position: absolute; top: 138px; left: 0; right: 0;
    font-family: "Oswald", sans-serif; font-weight: 300;
    font-size: 58px; letter-spacing: 5px; line-height: 1;
    background: linear-gradient(180deg, #f3dc9e 0%, var(--gold) 45%, var(--gold-dark) 100%);
    -webkit-background-clip: text; background-clip: text; color: transparent;
  }
  .festival-kind {
    position: absolute; top: 272px; left: 0; right: 0;
    font-family: "Oswald", sans-serif; font-weight: 500;
    font-size: 62px; letter-spacing: 3px; line-height: 1;
    color: var(--silver); opacity: .88;
  }
  .festival-dates {
    position: absolute; top: 380px; left: 0; right: 0;
    font-family: "Oswald", sans-serif; font-weight: 500;
    font-size: 28px; letter-spacing: 5px; color: #1a2a2c;
  }
  .season-year {
    position: absolute; top: 480px; left: 0; right: 0;
    font-family: "Oswald", sans-serif; font-weight: 400;
    font-size: 350px; line-height: 1; letter-spacing: 4px;
    color: var(--year-fill);
    -webkit-text-stroke: 5px var(--year-edge);
    text-shadow: 0 0 30px rgba(240,180,120,.35), 4px 6px 10px rgba(0,0,0,.6);
  }
  .site-address {
    position: absolute; top: 950px; left: 0; right: 0;
    font-family: "Oswald", sans-serif; font-weight: 400;
    font-size: 19px; letter-spacing: 1px; color: var(--sky-text);
  }
  .genre-box {
    position: absolute; left: 48px; top: 985px; width: 646px; height: 122px;
    border: 2px solid var(--box-line);
    display: flex; flex-direction: column; justify-content: center;
    font-family: "Cormorant Garamond", serif; font-weight: 600;
    font-size: 33px; line-height: 1.25; letter-spacing: 1px;
    color: var(--genre);
  }
</style>
</head>
<body>
  <main class="poster">
    <div class="scene-art" role="img" aria-label="Dusky photograph of two silhouetted musicians flanking a glowing city skyline"></div>
    <h1 class="festival-name">FERN LEDGE MAPLECREST</h1>
    <h2 class="festival-kind">MUSIC FESTIVAL</h2>
    <p class="festival-dates">JULY 29 - AUGUST 7</p>
    <p class="season-year">2016</p>
    <p class="site-address">WWW.FERNLEDGEMAPLECRESTFEST.EXAMPLE</p>
    <div class="genre-box">
      <span>JAZZ I CHORAL I CABARET I EDUCATION</span>
      <span>BROADWAY I CHAMBER I OPERA</span>
    </div>
  </main>
</body>
</html>
```